Whitcombe MD Crest Primary Care Business Card

Need a business card for a medical clinic targeting VIP patients. Should portray an upscale feeling. Simple, clean design. Logo and colors need to be incorporated into card. Clinic colors are gray/ silver, blues, white same as logo.
Clinic is a cash only VIP service clinic targeting higher income patients.
Tagline: "Where everyone is a VIP - Very Important Patient"

Target Market(s)

VIP, upscale

Industry/Entity Type

Medical

Contact Information for Business Card

Would like to use for cards with raised print or metallic highlight.

Requirements
Must have
• Incorporate logo, Use colors in logo
Nice to have
• Metallic detail
Should not have
• too much details or colors, other stock photos or designs

```html
<!DOCTYPE html>
<html lang="en">
<head>
<meta charset="utf-8">
<title>Whitcombe MD Crest Primary Care – Business Card</title>
<link rel="stylesheet" href="https://fonts.googleapis.com/css2?family=Cinzel:wght@400;600&family=Lora:wght@400&display=swap">
<style>
  :root {
    --stage: #c9c9c9;
    --navy: #34475a;
    --navy-light: #6b7780;
    --silver: #eef0f0;
    --paper: #f7f7f7;
    --ink: #2f3f52;
    --steel: #848c8f;
    --muted: #55606b;
  }
  * { margin: 0; padding: 0; box-sizing: border-box; }
  html, body { width: 1200px; height: 576px; overflow: hidden; }
  body { background: var(--stage); position: relative; font-family: "Lora", Georgia, serif; }

  .card {
    position: absolute; top: 138px; width: 484px; height: 294px;
    border-radius: 14px; overflow: hidden;
  }

  /* Front */
  .card-front {
    left: 82px;
    background: linear-gradient(180deg, var(--navy) 0%, var(--navy) 40%, var(--navy-light) 100%);
    color: #f2f3f4; text-align: center;
  }
  .front-mark {
    position: absolute; top: 96px; left: 0; right: 0;
    font-family: "Cinzel", serif; font-weight: 400; font-size: 34px; letter-spacing: 2px;
  }
  .front-name {
    position: absolute; top: 180px; left: 0; right: 0;
    display: flex; align-items: center; justify-content: center; gap: 10px;
    font-family: "Cinzel", serif; font-size: 25px; line-height: 1;
  }
  .front-name::before, .front-name::after {
    content: ""; width: 40px; height: 1.5px; background: #f2f3f4;
  }
  .front-tagline {
    position: absolute; top: 208px; left: 0; right: 0;
    font-family: "Cinzel", serif; font-size: 22px; letter-spacing: 0.5px;
  }

  /* Back */
  .card-back {
    left: 602px;
    background: linear-gradient(180deg, var(--paper) 0%, var(--silver) 100%);
    color: var(--ink);
  }
  .back-mark {
    position: absolute; left: 34px; top: 128px; width: 180px; text-align: center;
    font-family: "Cinzel", serif; font-size: 26px; color: var(--ink);
  }
  .back-details { position: absolute; left: 256px; top: 76px; }
  .holder-name { font-family: "Cinzel", serif; font-weight: 600; font-size: 18px; letter-spacing: 0.5px; white-space: nowrap; }
  .holder-role { font-size: 11.5px; color: var(--muted); margin-top: 6px; }
  .contact-list { list-style: none; margin-top: 20px; font-size: 12px; line-height: 16px; }
  .contact-list li { display: flex; align-items: center; gap: 12px; }
  .contact-list svg { width: 11px; height: 11px; fill: #6b747c; }
  .address { font-size: 12px; line-height: 16px; margin-top: 4px; }

  .band-steel {
    position: absolute; left: 0; bottom: 0; width: 210px; height: 16px; background: var(--steel);
  }
  .band-navy {
    position: absolute; right: 0; bottom: 0; width: 280px; height: 32px; background: var(--navy);
    clip-path: polygon(18px 0, 100% 0, 100% 100%, 0 100%);
    color: #e7eaec; font-size: 12px; display: flex; align-items: center; justify-content: center;
    padding-left: 14px;
  }
</style>
</head>
<body>
  <section class="card card-front">
    <div class="front-mark">Whitcombe</div>
    <div class="front-name">Whitcombe MD</div>
    <div class="front-tagline">Crest Primary Care</div>
  </section>

  <section class="card card-back">
    <div class="back-mark">Whitcombe</div>
    <div class="back-details">
      <div class="holder-name">WHITCOMBE CREST</div>
      <div class="holder-role">Managing Director</div>
      <ul class="contact-list">
        <li>
          <svg viewBox="0 0 10 10"><path d="M1 3.5C1 2 2 1.5 5 1.5S9 2 9 3.5H7V2.8H3V3.5ZM2 4.5H8L9 8.5H1Z"/></svg>
          801-555-0142
        </li>
        <li>
          <svg viewBox="0 0 10 10"><path d="M2.5 1H7.5V3.5H2.5ZM1 4H9V7.5H7.5V6H2.5V7.5H1ZM3 6.5H7V9H3Z"/></svg>
          name@whitcombecrest.com
        </li>
      </ul>
      <p class="address">48 Harbor Ridge Lane<br>Maple Falls City 84021</p>
    </div>
    <div class="band-steel"></div>
    <div class="band-navy">www.whitcombecrest.com</div>
  </section>
</body>
</html>
```